A online shop for solid wood need a Stationary design

A new online shop (in Austria and Germany) for solid wood and steel furniture (feldmark-tischwerk) needs a Stationay design (letterhead, business card, envelope etc...). Dining tables, coffee tables, TV furniture and similar furniture will be sold. Everything will be custom made.

```html
<!DOCTYPE html>
<html lang="en">
<head>
<meta charset="utf-8">
<title>Feldmark Tischwerk – Letterhead</title>
<link rel="stylesheet" href="https://fonts.googleapis.com/css2?family=Lato:wght@400;700;900&family=Josefin+Sans:wght@400&family=Tangerine:wght@700&display=swap">
<style>
  :root {
    --brand-red: #e20a17;
    --ink: #3a3a3a;
    --ink-dark: #2b2b2b;
    --band-black: #1e1e1e;
    --paper: #ffffff;
    --paper-shade: #f1f1f3;
    --backdrop: #e8e8e8;
  }
  * { margin: 0; padding: 0; box-sizing: border-box; }
  html, body {
    width: 1154px; height: 1200px; overflow: hidden;
    background: var(--backdrop);
  }
  .letterhead {
    position: absolute; left: 167px; top: 20px;
    width: 820px; height: 1160px;
    background: radial-gradient(ellipse at 50% 30%, var(--paper) 0%, var(--paper-shade) 100%);
    box-shadow: 0 2px 8px rgba(0,0,0,0.25);
    overflow: hidden;
    font-family: 'Lato', sans-serif;
    color: var(--ink);
  }
  .brand {
    position: absolute; left: 70px; top: 50px; width: 180px;
    display: flex; flex-direction: column; align-items: center;
    color: var(--brand-red); font-weight: 900;
  }
  .brand-square {
    width: 62px; height: 62px; background: var(--brand-red); margin-bottom: 18px;
  }
  .brand-name { font-size: 29px; letter-spacing: 1px; line-height: 1; }
  .brand-sub { font-size: 10.5px; letter-spacing: 5px; margin-top: 6px; line-height: 1; }

  .contact {
    position: absolute; left: 567px; top: 51px;
    border-left: 1.5px solid var(--brand-red);
    padding-left: 11px; height: 94px;
    font-family: 'Josefin Sans', sans-serif; font-size: 13px;
    color: var(--ink-dark); line-height: 18px;
  }
  .contact-address { margin-bottom: 5px; }
  .contact-row { display: flex; align-items: center; gap: 4px; }
  .contact-row svg { width: 11px; height: 11px; fill: var(--brand-red); flex: none; }

  .letter { position: absolute; left: 70px; top: 255px; width: 692px; font-size: 14.6px; line-height: 17.7px; }
  .letter-date { font-size: 15.5px; margin-bottom: 28px; }
  .recipient { font-size: 15.5px; line-height: 19px; margin-bottom: 18px; }
  .salutation { font-size: 18.5px; font-weight: 700; color: var(--ink-dark); margin: 14px 0 22px; }
  .letter-body p { text-align: justify; margin-bottom: 17.5px; }
  .closing { font-size: 15px; margin-top: 38px; }
  .signature {
    font-family: 'Tangerine', cursive; font-size: 44px; font-weight: 700;
    color: var(--ink-dark); margin-top: 22px; line-height: 1;
  }

  .footer-wave { position: absolute; left: 0; bottom: 0; width: 820px; height: 108px; display: block; }
</style>
</head>
<body>
  <main class="letterhead">
    <header>
      <div class="brand">
        <div class="brand-square"></div>
        <div class="brand-name">FELDMARK</div>
        <div class="brand-sub">TISCHWERK</div>
      </div>
      <address class="contact" style="font-style:normal">
        <div class="contact-address">P.O Box 4716-00210<br>Linz, Austria</div>
        <div class="contact-row">
          <svg viewBox="0 0 24 24"><path d="M2 9c0-4 4-6 10-6s10 2 10 6v2h-6V8H8v3H2zM5 13h14l2 8H3z"/></svg>
          986-555-0142
        </div>
        <div class="contact-row">
          <svg viewBox="0 0 24 24"><path d="M2 5h20v14H2zM3 6l9 7 9-7v2l-9 7-9-7z" fill-rule="evenodd"/></svg>
          info@feldmarktischwerk.com
        </div>
        <div class="contact-row">
          <svg viewBox="0 0 24 24"><circle cx="12" cy="12" r="10"/><path d="M6 8c3 0 4 2 3 4s1 4 0 6M14 4c0 3 3 3 4 5s-2 3-1 6" stroke="#fff" stroke-width="1.6" fill="none"/></svg>
          www.feldmarktischwerk.com
        </div>
      </address>
    </header>

    <section class="letter">
      <p class="letter-date">Feb-03-2022</p>
      <p class="recipient">Mr, Jonas Hale<br>President</p>
      <p class="recipient">Norvale Corporation<br>123 Street Name, Suite# 10<br>City, State, 120023</p>
      <h1 class="salutation">Dear Mr, Jonas</h1>
      <div class="letter-body">
        <p>Lorem ipsum dolor sit amet, consectetur adipisicing elit, sed do eiusmod tempor incididunt ut labore et dolore magna aliqua. Ut enim ad minim veniam, quis nostrud exercitation ullamco laboris nisi ut aliquip ex ea commodo consequat. Duis aute irure dolor in reprehenderit in voluptate velit esse cillum dolore eu fugiat nulla pariatur.</p>
        <p>Lorem ipsum dolor sit amet, consectetur adipisicing elit, sed do eiusmod tempor incididunt ut labore et dolore magna aliqua. Ut enim ad minim veniam, quis nostrud exercitation ullamco laboris nisi ut aliquip ex ea commodo consequat. Duis aute irure dolor in reprehenderit in voluptate velit esse cillum dolore eu fugiat nulla pariatur.</p>
        <p>Lorem ipsum dolor sit amet, consectetur adipisicing elit, sed do eiusmod tempor incididunt ut labore et dolore magna aliqua. Ut enim ad minim veniam, quis nostrud exercitation ullamco laboris nisi ut aliquip ex ea commodo consequat.</p>
        <p>Excepteur sint occaecat cupidatat non proident, sunt in culpa qui officia deserunt mollit anim id est laborum. re et dolore magnam aliquam quaerat voluptatem.</p>
      </div>
      <p class="closing">Regards</p>
      <p class="signature">Lukas Berger</p>
    </section>

    <svg class="footer-wave" viewBox="0 1600 1248 165" preserveAspectRatio="none" aria-hidden="true">
      <path d="M650 1660 C900 1700 1100 1680 1248 1594 V1630 C1100 1705 900 1712 650 1660 Z" fill="var(--band-black)"/>
      <path d="M0 1667 C250 1600 500 1610 800 1682 C1000 1722 1150 1692 1248 1640 V1765 H0 Z" fill="var(--brand-red)" stroke="#ffffff" stroke-width="7"/>
    </svg>
  </main>
</body>
</html>
```